Paper Orchards (instructional dating book)

Title: Paper Orchards
Subtitle: Ways to charm a stranger across any crowded room
Author: R.J. Pollard
I'm seeking the title to be central with the subtitle underneath and the author slightly lower and to the left. Perhaps a border or two around the font. I thought the background could look aged (off color and old textured paper) and the background slightly punched into the texture like a typewriter has been used. I imagine it something like an old Fenwright playbook or 1940s morse code manual. Many thanks!

Target Market(s)

18 to 45 year old single people

Industry/Entity Type

Dating

Font styles to use
Serif

Requirements
Must have
• Text with border or two
Nice to have
• Traditional feel. The book is instructional.
Should not have
• Too much color or flair

```html
<!DOCTYPE html>
<html lang="en">
<head>
<meta charset="utf-8">
<title>Paper Orchards — R.J. Pollard</title>
<link rel="stylesheet" href="https://fonts.googleapis.com/css2?family=Special+Elite&display=swap">
<style>
  :root {
    --paper-light: #e6dcc6;
    --paper-mid: #d9cbb0;
    --paper-stain: #b8996c;
    --paper-edge: #a98a5e;
    --ink: #3b2616;
    --rule: #4e3422;
    --rule-soft: #7a5c44;
  }
  html, body {
    margin: 0;
    padding: 0;
    width: 873px;
    height: 1200px;
    overflow: hidden;
    background: var(--paper-light);
  }
  .cover {
    position: relative;
    width: 873px;
    height: 1200px;
    overflow: hidden;
    font-family: "Special Elite", "Courier New", monospace;
    color: var(--ink);
  }
  .paper-texture {
    position: absolute;
    inset: 0;
    background:
      radial-gradient(ellipse 260px 200px at 30px 40px, rgba(169,138,94,.55), transparent 70%),
      radial-gradient(ellipse 240px 320px at 860px 120px, rgba(169,138,94,.5), transparent 70%),
      radial-gradient(ellipse 220px 300px at 20px 1150px, rgba(169,138,94,.45), transparent 70%),
      radial-gradient(ellipse 300px 240px at 860px 1180px, rgba(169,138,94,.5), transparent 70%),
      radial-gradient(ellipse 180px 120px at 620px 300px, rgba(184,153,108,.25), transparent 70%),
      radial-gradient(ellipse 200px 140px at 240px 860px, rgba(184,153,108,.25), transparent 70%),
      radial-gradient(ellipse 160px 110px at 520px 980px, rgba(184,153,108,.2), transparent 70%),
      radial-gradient(ellipse 700px 800px at 436px 560px, var(--paper-light), var(--paper-mid) 85%);
  }
  .title-frame {
    position: absolute;
    left: 92px;
    top: 512px;
    width: 690px;
    height: 215px;
    box-sizing: border-box;
    border: 3px solid var(--rule);
  }
  .title-frame::before {
    content: "";
    position: absolute;
    inset: 5px;
    border: 1px solid var(--rule-soft);
  }
  .title {
    position: absolute;
    left: 0;
    right: 0;
    top: 40px;
    margin: 0;
    text-align: center;
    font-family: inherit;
    font-weight: 400;
    font-size: 68px;
    line-height: 1;
    letter-spacing: 2px;
  }
  .subtitle {
    position: absolute;
    left: 0;
    right: 0;
    top: 138px;
    margin: 0;
    text-align: center;
    font-size: 19px;
    line-height: 1;
    -webkit-text-stroke: 0.4px var(--ink);
  }
  .author {
    position: absolute;
    left: 132px;
    top: 1082px;
    margin: 0;
    font-size: 21px;
    line-height: 1;
    -webkit-text-stroke: 0.4px var(--ink);
  }
</style>
</head>
<body>
  <main class="cover">
    <div class="paper-texture" role="img" aria-label="Aged, stained off-white paper texture"></div>
    <section class="title-frame">
      <h1 class="title">Paper Orchards</h1>
      <p class="subtitle">Ways to charm a stranger across any crowded room</p>
    </section>
    <p class="author">R.J. Pollard</p>
  </main>
</body>
</html>
```